General Contractors need a new Crisp updated Card Design

We need a new business card design for our company of 25 years based in Toronto call Pollvarn Building Inc. : Our goal is to be the leading commercial contractors in Toronto by providing exceptional value to our clients. We work very hard to deliver professional, quality, service in conjunction with consistent price competitiveness to all of our clients on every single project.

Target Market(s)

Design & Build Clients

Industry/Entity Type

Construction Company

Contact Information for Business Card

Address:
18 West Marlow Field Road, Unit 17, Dunmore Vale, ON, K7T 2M9
Office: 905-218-6937

Pollvarns Logo
Employee Job Description
Employee Cell Phone #
Employee Email
www.pollvarn.example

Colors

Designer to choose colors to be used in the design.

Requirements
Must have
• Quote Company Saying:
• "Professional. Quality. Service."
Nice to have
• New Crisp up to date look. simple & fresh ( Not to Busy)
Should not have
• NO BLUE PRINTS ON THE BUSINESS CARDS

```html
<!DOCTYPE html>
<html lang="en">
<head>
<meta charset="utf-8">
<title>Pollvarn Building Inc. – Business Card</title>
<link rel="stylesheet" href="https://fonts.googleapis.com/css2?family=Libre+Baskerville:ital,wght@0,400;0,700;1,400&family=Open+Sans:ital,wght@1,400&display=swap">
<style>
  :root {
    --backdrop: #2b2d31;
    --card-dark: #221f20;
    --card-light: #ffffff;
    --teal: #0f5f57;
    --sage: #8fa99e;
    --ink: #333333;
    --ink-soft: #5a5a5a;
    --tagline: #b9bdbb;
  }
  * { box-sizing: border-box; margin: 0; padding: 0; }
  html, body {
    width: 1200px; height: 900px; overflow: hidden;
    background: var(--backdrop);
  }
  .canvas { position: relative; width: 1200px; height: 900px; }

  .card {
    position: absolute; width: 525px; height: 300px;
    box-shadow: 0 10px 30px rgba(0,0,0,.35);
  }

  /* Front: dark side with company name */
  .card-front {
    left: 70px; top: 440px; background: var(--card-dark);
  }
  .brand {
    position: absolute; left: 60px; top: 82px;
    display: flex; align-items: center; gap: 18px;
  }
  .brand-square { width: 62px; height: 62px; background: var(--teal); flex: none; }
  .brand-name {
    font-family: "Libre Baskerville", Georgia, serif; font-weight: 700;
    font-size: 27px; letter-spacing: 1px; line-height: 1.2; color: var(--teal);
    text-transform: uppercase;
  }
  .tagline {
    position: absolute; left: 0; right: 0; top: 210px; text-align: center;
    font-family: "Open Sans", Arial, sans-serif; font-style: italic;
    font-size: 17px; color: var(--tagline); letter-spacing: .3px;
  }

  /* Back: white side with contact details */
  .card-back {
    left: 605px; top: 150px; background: var(--card-light);
    border-left: 16px solid var(--teal);
  }
  .person { position: absolute; left: 26px; top: 24px; }
  .person-name {
    font-family: "Libre Baskerville", Georgia, serif; font-weight: 700;
    font-size: 19px; color: var(--teal); letter-spacing: .5px;
  }
  .person-role {
    font-family: "Libre Baskerville", Georgia, serif;
    font-size: 11px; color: var(--ink); letter-spacing: .8px; margin-top: 2px;
  }
  .contact-list {
    position: absolute; left: 26px; top: 112px; list-style: none;
    font-family: "Libre Baskerville", Georgia, serif; font-size: 13px; color: var(--ink-soft);
  }
  .contact-list li { display: flex; align-items: center; gap: 10px; height: 22px; }
  .contact-list svg { width: 13px; height: 13px; fill: var(--teal); flex: none; }
  .mark-square {
    position: absolute; right: 30px; top: 95px; width: 112px; height: 112px;
    background: var(--teal);
  }
  .address {
    position: absolute; right: 30px; bottom: 26px; text-align: right;
    font-family: "Libre Baskerville", Georgia, serif; font-style: italic;
    font-size: 12.5px; line-height: 1.6; color: var(--ink-soft);
  }
</style>
</head>
<body>
<main class="canvas">

  <section class="card card-front" aria-label="Card front">
    <div class="brand">
      <span class="brand-square"></span>
      <span class="brand-name">Pollvarn<br>Building Inc.</span>
    </div>
    <p class="tagline">“Professional. Quality. Service.”</p>
  </section>

  <section class="card card-back" aria-label="Card back">
    <div class="person">
      <p class="person-name">MAREK TOLLAN</p>
      <p class="person-role">OWNER</p>
    </div>

    <ul class="contact-list">
      <li>
        <svg viewBox="0 0 16 16" aria-hidden="true"><path d="M3 1h3l1.5 4-2 1.3a9 9 0 0 0 4.2 4.2L11 8.5l4 1.5v3a2 2 0 0 1-2 2A12 12 0 0 1 1 3a2 2 0 0 1 2-2z"/></svg>
        905-218-6937
      </li>
      <li>
        <svg viewBox="0 0 16 16" aria-hidden="true"><path d="M4 0h8a1 1 0 0 1 1 1v14a1 1 0 0 1-1 1H4a1 1 0 0 1-1-1V1a1 1 0 0 1 1-1zm.8 1.6v10.8h6.4V1.6zM8 13.2a.9.9 0 1 0 0 1.8.9.9 0 0 0 0-1.8z"/></svg>
        123 - xxx - xxx
      </li>
      <li>
        <svg viewBox="0 0 16 16" aria-hidden="true"><path d="M1 3h14v10H1zm1.4 1.2L8 8.6l5.6-4.4z"/></svg>
        email@pollvarn.example
      </li>
      <li>
        <svg viewBox="0 0 16 16" aria-hidden="true"><path d="M8 0a8 8 0 1 0 0 16A8 8 0 0 0 8 0zm0 1.5c.9 0 2 1.8 2.3 5.5H5.7C6 3.3 7.1 1.5 8 1.5zM1.6 7h2.6c.1-2 .5-3.6 1.1-4.7A6.5 6.5 0 0 0 1.6 7zm10.2 0h2.6a6.5 6.5 0 0 0-3.7-4.7c.6 1.1 1 2.7 1.1 4.7zM1.6 9a6.5 6.5 0 0 0 3.7 4.7C4.7 12.6 4.3 11 4.2 9zm4.1 0c.3 3.7 1.4 5.5 2.3 5.5s2-1.8 2.3-5.5zm6.1 0c-.1 2-.5 3.6-1.1 4.7A6.5 6.5 0 0 0 14.4 9z"/></svg>
        www.pollvarn.example
      </li>
    </ul>

    <span class="mark-square" aria-hidden="true"></span>

    <address class="address">
      18 West Marlow Field Road, Unit 17<br>
      Dunmore Vale, ON, K7T 2M9
    </address>
  </section>

</main>
</body>
</html>
```